Professional Organizing Services & Store
Keen Nest Works - Bus Cards, Stationery, Envelope
Professional Organizing Services & Store - Consulting
Creative Brief
Professional
Marla Fenwick, Certified Professional Organzier
Motivational Speaker & Creator of Desk Heaps Gone Quick(r)
517 Orchard Lane Emmaus, PA 18049 Suite 4100 742 Heron Avenue West Palm Beach, FL 33401
(610) 555-0193 (561) xxx-xxxx
Organize@MarlaFenwick.example
www.MarlaFenwick.example
Please see attached document for details. We need two business cards with similar layouts
Keen Nest Works is a full service professional organizing firm providing one-on-one consultation services and services by a team of professional organizers. Founded in Allentown, Pennsylvania Keen Nest Works serves the tri-state area and a second office serves Florida. Our organizers travel nationally and work with clients virtually. Residential – Whole House (Bullets can be changed/eliminated) Papers ♦ Closet s ♦ Unpack & Setup ♦ High Performance Families ♦ Organizing Makeovers Small Business & Corporate Organizing & Productivity ♦ Paper & Time Management Speaking Engagements Keynote, Workshops, & Training

```html
<!DOCTYPE html>
<html lang="en">
<head>
<meta charset="utf-8">
<title>Keen Nest Works – Business Cards</title>
<link href="https://fonts.googleapis.com/css2?family=Arimo:ital,wght@0,400;0,700;1,400;1,700&display=swap" rel="stylesheet">
<style>
  :root {
    --page: #e8e4df;
    --card: #ffffff;
    --plum: #5f4360;
    --plum-deep: #5a4058;
    --green: #4f8a2a;
    --ink: #2f2a2f;
    --muted: #9a9a9a;
    --on-plum: #f3edf3;
  }
  * { box-sizing: border-box; margin: 0; padding: 0; }
  html, body { width: 1200px; height: 852px; overflow: hidden; }
  body {
    background: var(--page);
    position: relative;
    font-family: "Arimo", Arial, sans-serif;
    color: var(--ink);
  }
  .card {
    position: absolute;
    border-radius: 14px;
    overflow: hidden;
    background: var(--card);
    box-shadow: 0 6px 14px rgba(0,0,0,.25);
  }
  /* front */
  .card-front { left: 348px; top: 96px; width: 504px; height: 368px; }
  .brand {
    position: absolute; top: 62px; left: 0; right: 0;
    display: flex; align-items: center; justify-content: center; gap: 12px;
  }
  .brand-mark { width: 16px; height: 16px; background: var(--plum); }
  .brand-name { font-weight: 700; font-size: 30px; color: var(--plum); }
  .person { position: absolute; top: 170px; left: 0; right: 0; text-align: center; }
  .person-name { font-weight: 700; font-size: 22px; color: var(--plum); }
  .person-title { font-weight: 700; font-size: 14px; color: var(--green); margin-top: 8px; }
  .person-role { font-weight: 700; font-style: italic; font-size: 12.5px; color: var(--plum); margin-top: 4px; }
  .rule { position: absolute; top: 242px; left: 0; right: 0; height: 2px; background: #cfcfcf; }
  .contact-band {
    position: absolute; left: 0; right: 0; top: 248px; bottom: 0;
    background: var(--plum); color: var(--on-plum);
    display: flex; justify-content: center; align-items: center; gap: 14px;
    font-size: 12.5px; line-height: 1.55;
  }
  .addresses { text-align: right; }
  .addresses p + p { margin-top: 6px; }
  .divider { width: 1px; align-self: stretch; margin: 20px 0; background: var(--on-plum); }
  /* backs */
  .card-back { top: 504px; width: 528px; height: 312px; padding: 22px 28px; font-size: 11px; line-height: 1.55; }
  .card-back.light { left: 60px; }
  .card-back.dark { left: 629px; background: var(--plum-deep); color: var(--on-plum); }
  .intro { margin-bottom: 6px; }
  .service-head { font-weight: 700; font-size: 13.5px; color: var(--plum); margin-top: 2px; }
  .dark .service-head { color: #fff; }
  .service-list { list-style: none; display: flex; flex-wrap: wrap; column-gap: 14px; padding-left: 8px; font-size: 12px; }
  .service-list li::before { content: "\2022"; margin-right: 6px; }
  .service-list .break { flex-basis: 100%; height: 0; }
  .notes { display: flex; align-items: flex-end; gap: 6px; font-weight: 700; font-size: 12px; color: var(--plum); margin-top: 2px; }
  .dark .notes { color: #fff; }
  .notes span.line { flex: 1; border-bottom: 1px solid currentColor; margin-bottom: 3px; }
  .blank-line { border-bottom: 1px solid var(--muted); height: 18px; }
  .dark .blank-line { border-color: #b8a4b8; }
</style>
</head>
<body>

<section class="card card-front">
  <div class="brand">
    <span class="brand-mark"></span>
    <span class="brand-name">Keen Nest Works</span>
  </div>
  <div class="person">
    <p class="person-name">Marla Fenwick</p>
    <p class="person-title">Certified Professional Organizer</p>
    <p class="person-role">Motivational Speaker &amp; Creator of Desk Heaps Gone Quick(r)</p>
  </div>
  <div class="rule"></div>
  <div class="contact-band">
    <div class="addresses">
      <p>517 Orchard Lane Emmaus<br>PA 18049</p>
      <p>Suite 4100 742 Heron Avenue<br>West Palm Beach, FL 33401</p>
    </div>
    <div class="divider"></div>
    <div class="contacts">
      <p>T : (610) 555-0193 (561)</p>
      <p>F : (610) 555-0148</p>
      <p>E : Organize@MarlaFenwick.example</p>
      <p>www.MarlaFenwick.example</p>
    </div>
  </div>
</section>

<section class="card card-back light">
  <p class="intro">Keen Nest Works is a full service professional organizing firm providing one-on-one consultation services and services by a team of professional organizers. Founded in Allentown, Pennsylvania Keen Nest Works serves the tri-state area and a second office serves Florida. Our organizers travel nationally and work with clients virtually.</p>
  <p class="service-head">Residential</p>
  <ul class="service-list">
    <li>Whole House</li><li>Papers</li><li>Closets</li><li>Unpack &amp; Setup</li>
    <li class="break"></li>
    <li>High Performance Families</li><li>Organizing Makeovers</li>
  </ul>
  <p class="service-head">Small Business &amp; Corporate</p>
  <ul class="service-list"><li>Organizing &amp; Productivity</li><li>Paper &amp; Time Management</li></ul>
  <p class="service-head">Speaking Engagements</p>
  <ul class="service-list"><li>Keynote</li><li>Workshops</li><li>Training</li></ul>
  <p class="notes">Notes: <span class="line"></span></p>
  <div class="blank-line"></div>
</section>

<section class="card card-back dark">
  <p class="intro">Keen Nest Works is a full service professional organizing firm providing one-on-one consultation services and services by a team of professional organizers. Founded in Allentown, Pennsylvania Keen Nest Works serves the tri-state area and a second office serves Florida. Our organizers travel nationally and work with clients virtually.</p>
  <p class="service-head">Residential</p>
  <ul class="service-list">
    <li>Whole House</li><li>Papers</li><li>Closets</li><li>Unpack &amp; Setup</li>
    <li class="break"></li>
    <li>High Performance Families</li><li>Organizing Makeovers</li>
  </ul>
  <p class="service-head">Small Business &amp; Corporate</p>
  <ul class="service-list"><li>Organizing &amp; Productivity</li><li>Paper &amp; Time Management</li></ul>
  <p class="service-head">Speaking Engagements</p>
  <ul class="service-list"><li>Keynote</li><li>Workshops</li><li>Training</li></ul>
  <p class="notes">Notes: <span class="line"></span></p>
  <div class="blank-line"></div>
</section>

</body>
</html>
```